Website Re-Design

We would like to explore the possibility of a re-design of our website. We want all the content that it currently has to remain on the pages, and we don't want our logo/corporate identity or colours changed, so it is literally just a website re-design.

Our website is www.trovalink.co.uk

Websites that we like are

http://www.quillmarsh.co.uk/
http://rankwidget.com/

```html
<!DOCTYPE html>
<html lang="en">
<head>
<meta charset="utf-8">
<title>Trovalink — Inbound Marketing &amp; SEO</title>
<link rel="stylesheet" href="https://fonts.googleapis.com/css2?family=Open+Sans:wght@400;600;700;800&family=Oswald:wght@500;700&display=swap">
<style>
:root{
  --green:#8cc63f;
  --green-dark:#5f9a22;
  --green-deep:#3f7413;
  --pink:#e5007e;
  --ink:#333333;
  --muted:#777777;
  --line:#e2e2e2;
  --soft:#f3f3f3;
  --footer:#1d1d1d;
  --footer-base:#121212;
  --footer-text:#a9a9a9;
}
*{box-sizing:border-box;margin:0;padding:0}
html,body{width:1200px;height:3096px;overflow:hidden}
body{font-family:"Open Sans",Arial,sans-serif;color:var(--ink);background:#fff;position:relative}
.wrap{width:940px;margin:0 auto;position:relative}

/* header */
.site-header{height:60px;background:#fff;border-bottom:1px solid var(--line)}
.site-header .wrap{display:flex;align-items:center;justify-content:space-between;height:60px}
.brand{font-weight:800;font-size:26px;color:var(--green);letter-spacing:1px}
.main-nav{display:flex;gap:28px}
.main-nav a{font-size:12px;font-weight:700;color:var(--ink);text-decoration:none;padding:6px 0}
.main-nav a.is-active{color:var(--pink);border-bottom:3px solid var(--pink)}

/* hero */
.hero{position:relative;height:540px;overflow:hidden}
.hero-backdrop{position:absolute;inset:0;background:radial-gradient(circle at 50% 45%,#a8d95a 0%,#8cc63f 45%,#6aa82a 100%)}
.hero-seal{position:absolute;left:480px;top:72px}
.hero-list{position:absolute;top:150px;list-style:none;color:#fff;font-weight:700;font-size:19px;line-height:42px}
.hero-list--left{right:760px;text-align:right}
.hero-list--right{left:760px}

/* intro */
.intro{height:280px;padding-top:58px}
.intro h1{font-size:27px;font-weight:600;color:var(--pink);margin-bottom:20px}
.intro h1 span{color:var(--green-dark)}
.intro p{font-size:15px;line-height:25px;color:var(--muted)}

/* services */
.services{height:410px;background:var(--soft);border-top:1px solid var(--line);border-bottom:1px solid var(--line);padding-top:40px}
.services .wrap{display:flex;gap:35px}
.service{width:290px}
.service h2{font-size:17px;font-weight:800;color:var(--green-dark);text-transform:uppercase;margin-bottom:14px}
.service-media{height:160px;margin-bottom:16px}
.service p{font-size:13px;line-height:20px;color:var(--muted);height:62px;margin-bottom:18px}
.btn{display:inline-block;font-size:13px;font-weight:700;color:#fff;padding:8px 16px;text-decoration:none}
.btn--pink{background:var(--pink)}
.btn--green{background:var(--green-dark)}

/* section headings */
.section-title{font-size:29px;font-weight:600;color:var(--green-dark);padding-bottom:14px;border-bottom:1px solid var(--line);margin-bottom:34px;position:relative}
.code-mark{position:absolute;right:0;top:4px}

/* recent works */
.recent{height:350px;padding-top:50px}
.recent-body{display:flex;gap:60px}
.recent-media{width:430px;height:200px;background:linear-gradient(135deg,#2c2c2c 0%,#56585b 55%,#cfd3d6 100%)}
.recent-text{width:450px;font-size:14px;line-height:23px;color:var(--muted);padding-top:40px}

/* clients */
.clients{height:490px;background:var(--green);padding-top:54px;color:#fff}
.clients .section-title{color:#fff;border-bottom-color:rgba(255,255,255,.35);margin-bottom:20px}
.clients p{font-size:14px;line-height:23px;margin-bottom:44px}
.client-row{display:flex;gap:24px}
.client{width:169px;height:120px;background:#fff;display:flex;align-items:center;justify-content:center;font-size:17px;font-weight:700;color:var(--ink)}

/* call to action */
.cta{height:310px;padding-top:50px}
.cta h3{font-size:19px;font-weight:700;margin-bottom:10px}
.cta p{font-size:14px;line-height:23px;color:var(--muted);width:640px}
.cta-button{position:absolute;right:0;top:104px;font-family:"Oswald",Impact,sans-serif;font-weight:700;font-size:26px;color:#fff;background:var(--green-dark);padding:8px 22px;border:3px solid var(--green-deep);text-decoration:none;letter-spacing:1px}

/* footer */
.site-footer{height:600px;background:var(--footer);padding-top:60px;color:var(--footer-text)}
.site-footer .wrap{display:flex;gap:40px}
.footer-col{width:205px;font-size:13px;line-height:21px}
.footer-col h4{font-size:13px;font-weight:700;color:#fff;text-transform:uppercase;margin-bottom:18px}
.footer-links{list-style:none}
.footer-links li{padding:6px 0 6px 16px;border-bottom:1px solid #2e2e2e;position:relative}
.footer-links li::before{content:"›";position:absolute;left:0;color:var(--green)}
.footer-col p{margin-bottom:14px}
.footer-col a{color:var(--pink);text-decoration:none}
.search-box{display:flex;height:34px;border:1px solid #3a3a3a;background:#262626;margin-bottom:44px}
.search-box span{flex:1;padding:7px 10px;color:#777}
.search-box i{width:34px;display:flex;align-items:center;justify-content:center}
.socials{display:flex;gap:12px}
.socials span{width:38px;height:38px;border-radius:50%;background:#4a4a4a}
.socials span:first-child{background:var(--pink)}
.footer-base{height:56px;background:var(--footer-base);color:#8a8a8a;font-size:11px;line-height:17px;padding-top:11px}
</style>
</head>
<body>

<header class="site-header">
  <div class="wrap">
    <div class="brand">TROVALINK</div>
    <nav class="main-nav">
      <a class="is-active" href="#">HOME</a>
      <a href="#">ABOUT US</a>
      <a href="#">PORTFOLIO</a>
      <a href="#">WHAT WE DO</a>
      <a href="#">CONTACT US</a>
    </nav>
  </div>
</header>

<section class="hero">
  <div class="hero-backdrop" role="img" aria-label="Green backdrop scattered with faint marketing keyword tags"></div>
  <svg class="hero-seal" width="240" height="240" viewBox="0 0 240 240" aria-hidden="true">
    <circle cx="120" cy="120" r="118" fill="#5f9a22" opacity=".55"/>
    <circle cx="120" cy="120" r="100" fill="#3f7413"/>
    <line x1="50" y1="118" x2="190" y2="118" stroke="#8cc63f" stroke-width="2"/>
    <text x="120" y="104" text-anchor="middle" fill="#fff" font-family="Open Sans, sans-serif" font-weight="800" font-size="22">TROVALINK</text>
    <text x="120" y="166" text-anchor="middle" fill="#fff" font-family="Open Sans, sans-serif" font-weight="800" font-size="48">SEO</text>
  </svg>
  <ul class="hero-list hero-list--left">
    <li>Link Building</li>
    <li>Social Media</li>
    <li>Traffic Monitoring</li>
    <li>Content Generation</li>
    <li>Keyword Research</li>
  </ul>
  <ul class="hero-list hero-list--right">
    <li>URL Structure</li>
    <li>Site Promotion</li>
    <li>Strategic Interactions</li>
    <li>Optimized Content</li>
    <li>Site Construction</li>
  </ul>
</section>

<section class="intro">
  <div class="wrap">
    <h1>Trovalink <span>— your</span> inbound marketing &amp; SEO Performance agency</h1>
    <p>Do you want to earn your customers attention? Gain more visibility in the SERPs and build and engage with your audience? Trovalink specialises in SEO, Social media, CRO and Design &amp; Creative services. Offering a bespoke and personal service from a team of digital natives.</p>
  </div>
</section>

<section class="services">
  <div class="wrap">
    <article class="service">
      <h2>What can we do for you?</h2>
      <div class="service-media" role="img" aria-label="Consultant beside large SEO lettering" style="background:linear-gradient(120deg,#f7f7f7,#d9d9d9 60%,#c23a3a)"></div>
      <p>We offer a bespoke service and will customise to your needs. We specialise in progressive &amp; innovative solutions.</p>
      <a class="btn btn--pink" href="#">Read More ›</a>
    </article>
    <article class="service">
      <h2>See our portfolio</h2>
      <div class="service-media" role="img" aria-label="Bar chart graphic showing campaign growth" style="background:linear-gradient(180deg,#ffffff,#e8f3da 55%,#8cc63f)"></div>
      <p>Take a look at our case studies to see our recent campaigns showing results achieved for our clients.</p>
      <a class="btn btn--green" href="#">Read More ›</a>
    </article>
    <article class="service">
      <h2>Let's talk</h2>
      <div class="service-media" role="img" aria-label="Colourful infographic of connected speech bubbles" style="background:linear-gradient(135deg,#fdf3e1,#f4c27a 50%,#6fb6c9)"></div>
      <p>Use our form to send us a message, we will call you back as soon as we can.</p>
      <a class="btn btn--green" href="#">Read More ›</a>
    </article>
  </div>
</section>

<section class="recent">
  <div class="wrap">
    <h2 class="section-title">Recent Works
      <svg class="code-mark" width="34" height="30" viewBox="0 0 34 30" aria-hidden="true"><path d="M10 6 L2 15 L10 24 M24 6 L32 15 L24 24 M20 3 L14 27" fill="none" stroke="#8cc63f" stroke-width="2.5"/></svg>
    </h2>
    <div class="recent-body">
      <div class="recent-media" role="img" aria-label="Website shown on desktop, laptop, tablet and phone screens"></div>
      <p class="recent-text">Check out our recent works and case studies. These are a few examples to show the diversity of work that we can do to earn real attention, generate inbound links, mentions, citations and be used across many of our marketing channels. See more on our portfolio page and learn about what we could do for you.</p>
    </div>
  </div>
</section>

<section class="clients">
  <div class="wrap">
    <h2 class="section-title">Our Clients</h2>
    <p>We work with and represent a number of progressive companies in their SEO, social, inbound marketing, content and strategy needs.<br>Check out our case studies for examples.</p>
    <div class="client-row">
      <div class="client">Fernlot</div>
      <div class="client">Coachwell</div>
      <div class="client">Waypoint</div>
      <div class="client">Staylane</div>
      <div class="client" style="font-size:15px;text-align:center;line-height:20px">Image<br>coming<br>soon</div>
    </div>
  </div>
</section>

<section class="cta">
  <div class="wrap">
    <h2 class="section-title">Sound interesting?</h2>
    <h3>Interested in what you have seen so far?</h3>
    <p>Are you looking for a progressive and innovative inbound marketing agency who can work alongside your existing teams. If Yes, then let's have a chat.</p>
    <a class="cta-button" href="#">CONTACT US</a>
  </div>
</section>

<footer class="site-footer">
  <div class="wrap">
    <div class="footer-col">
      <h4>Useful Links</h4>
      <ul class="footer-links">
        <li>Home</li>
        <li>About</li>
        <li>Portfolio</li>
        <li>What We Do</li>
        <li>Contact us</li>
      </ul>
    </div>
    <div class="footer-col">
      <h4>About Us</h4>
      <p>Trovalink is an inbound marketing agency offering a raft of services from digital strategy and planning through to SEO, Social media, SMM, CRO, Design &amp; Creative through to paid for performance campaigns.</p>
      <p><a href="#">Talk to us</a> to discuss your needs.</p>
    </div>
    <div class="footer-col">
      <h4>Where are we?</h4>
      <p>We are in London, UK, based down the road here in Little Venice, so come check it out and walk the canals with us or we're happy to venture to you!</p>
      <h4 style="margin-top:26px">UK Office</h4>
      <p>14 Harrow Mews, Little Venice, London, W9 3QA</p>
      <p>Phone: +44 (0) 20 7946 0321</p>
      <p>Email: <a href="#">hello@trovalink.co.uk</a></p>
    </div>
    <div class="footer-col">
      <h4>Search this site</h4>
      <div class="search-box"><span>Search</span><i><svg width="14" height="14" viewBox="0 0 14 14" aria-hidden="true"><circle cx="6" cy="6" r="4.5" fill="none" stroke="#999" stroke-width="1.6"/><line x1="9.5" y1="9.5" x2="13" y2="13" stroke="#999" stroke-width="1.6"/></svg></i></div>
      <h4>Search this site</h4>
      <div class="socials"><span></span><span></span><span></span><span></span></div>
    </div>
  </div>
</footer>

<div class="footer-base">
  <div class="wrap">Copyright © 2013 Trovalink. All Rights Reserved. Trovalink is the trading name of Trovalink Limited, registered in the UK at Companies House<br>0000000, and VAT registered 000 0000 00.</div>
</div>

</body>
</html>
```